Real Estate Company / Capital Needs Cards!

need business cards designed using the logos that were just designed by sketchhive.

Reason: per designers request deadline extended 1 day…thank you.

Target Market(s)

Investors and clients looking to purchase real estate or invest in the business.

Industry/Entity Type

Business

Requirements
Must have
• two designs - one for the real estate logo and one for the capital logo, similar but slightly different.
Nice to have
• something to make it pop (perhaps on the back)
Should not have
• much color

```html
<!DOCTYPE html>
<html lang="en">
<head>
<meta charset="utf-8">
<title>Realtor and Capital Business Cards</title>
<link href="https://fonts.googleapis.com/css2?family=Open+Sans:wght@300;400;600&display=swap" rel="stylesheet">
<style>
  :root {
    --backdrop: #141414;
    --card-dark: #3b393a;
    --card-dark-edge: #2e2c2d;
    --panel-light: #f3f3f3;
    --skyline-tone: #dcdcdc;
    --ink-dark: #1f1f1f;
    --ink-light: #f4f4f4;
    --ink-muted: #c9c9c9;
    --accent-gold: #d8ccae;
    --accent-gold-deep: #b9a983;
    --stitch: #9d9b9c;
  }
  * { margin: 0; padding: 0; box-sizing: border-box; }
  html, body {
    width: 1200px; height: 800px; overflow: hidden;
    background: var(--backdrop);
    font-family: "Open Sans", Arial, sans-serif;
  }
  .stage {
    position: relative; width: 1200px; height: 800px;
  }
  .card {
    position: absolute; top: 130px;
    width: 310px; height: 540px;
    background: var(--card-dark);
    box-shadow: 0 18px 40px rgba(0,0,0,0.6);
    overflow: hidden;
  }
  .card--realtor { left: 235px; }
  .card--capital { left: 655px; }

  /* Realtor front */
  .realtor-header {
    height: 92px; text-align: center; color: var(--ink-light);
    padding-top: 34px;
  }
  .realtor-name { font-size: 19px; font-weight: 400; letter-spacing: 0.5px; line-height: 1; }
  .realtor-role { font-size: 10px; font-weight: 400; margin-top: 4px; color: var(--ink-muted); }
  .realtor-panel {
    position: relative; height: 290px; background: var(--panel-light);
  }
  .skyline-art {
    position: absolute; left: 0; right: 0; top: 0; bottom: 0;
    background: linear-gradient(180deg, var(--panel-light) 0%, var(--skyline-tone) 55%, var(--panel-light) 100%);
  }
  .studio-block {
    position: absolute; right: 22px; bottom: 24px; text-align: right; color: var(--ink-dark);
  }
  .studio-name { font-size: 18px; font-weight: 400; letter-spacing: -0.2px; line-height: 1.1; }
  .studio-address { font-size: 11.5px; font-weight: 400; color: #333; margin-top: 2px; }
  .contact-list { padding: 26px 0 0 36px; list-style: none; }
  .contact-item {
    display: flex; align-items: center; gap: 16px; margin-bottom: 18px;
    color: var(--ink-muted); font-size: 10.5px;
  }
  .contact-icon {
    width: 34px; height: 34px; border-radius: 50%; flex: none;
    background: radial-gradient(circle at 40% 35%, var(--accent-gold), var(--accent-gold-deep));
    display: flex; align-items: center; justify-content: center;
  }
  .contact-lines { line-height: 1.5; }

  /* Capital back */
  .stitch-frame {
    position: absolute; inset: 12px;
    border: 1px dashed var(--stitch);
  }
  .capital-brand {
    position: absolute; top: 150px; left: 0; right: 0;
    display: flex; flex-direction: column; align-items: center;
    color: var(--accent-gold); font-weight: 400;
  }
  .brand-square {
    width: 48px; height: 48px; background: var(--accent-gold); margin-bottom: 14px;
  }
  .brand-name { font-size: 30px; letter-spacing: 4px; line-height: 1; }
  .brand-suffix { font-size: 12px; letter-spacing: 2px; margin-top: 6px; }
</style>
</head>
<body>
<main class="stage">

  <article class="card card--realtor">
    <header class="realtor-header">
      <h1 class="realtor-name">YOUR NAME</h1>
      <p class="realtor-role">Realtor</p>
    </header>
    <section class="realtor-panel">
      <div class="skyline-art" role="img" aria-label="Light grey city skyline illustration of tall buildings"></div>
      <div class="studio-block">
        <p class="studio-name">MERIDIAN CARD STUDIO</p>
        <p class="studio-address">415 Harbor Lane, Ashford 20417</p>
      </div>
    </section>
    <ul class="contact-list">
      <li class="contact-item">
        <span class="contact-icon">
          <svg width="16" height="16" viewBox="0 0 24 24" aria-hidden="true"><path fill="#3b393a" d="M6.6 10.8a15 15 0 0 0 6.6 6.6l2.2-2.2a1 1 0 0 1 1-.25 11.4 11.4 0 0 0 3.6.57 1 1 0 0 1 1 1V20a1 1 0 0 1-1 1A17 17 0 0 1 3 4a1 1 0 0 1 1-1h3.5a1 1 0 0 1 1 1c0 1.25.2 2.45.57 3.6a1 1 0 0 1-.25 1z"/></svg>
        </span>
        <span class="contact-lines">+000 - 1234 - 5678</span>
      </li>
      <li class="contact-item">
        <span class="contact-icon">
          <svg width="16" height="16" viewBox="0 0 24 24" aria-hidden="true"><rect x="3" y="6" width="18" height="12" rx="1.5" fill="#3b393a"/><path d="M4 7l8 6 8-6" stroke="#d8ccae" stroke-width="1.5" fill="none"/></svg>
        </span>
        <span class="contact-lines">hello@meridiancard.com<br>www.meridiancard.com</span>
      </li>
    </ul>
  </article>

  <article class="card card--capital">
    <div class="stitch-frame"></div>
    <div class="capital-brand">
      <span class="brand-square"></span>
      <p class="brand-name">ALDER</p>
      <p class="brand-suffix">CAPITAL, LLC</p>
    </div>
  </article>

</main>
</body>
</html>
```